Website for New Business in Luxury Home Market

Build a website for a new business that is an off shoot of my primary business as an interior designer. These days, with Brimlo, QRMK and print media telling people they can be their own interior designer, General Contractors building a new home or remodeling, are frustrated because they do not get the information they need to be able to build or remodel. Clients/owners are often unaware that picking the pretty things like faucets, tile or appliances require specifications and drawings to tell the individual sub contractors how to proceed with their work, or to bid the project correctly. The professional interior designer used to fill this gap. Even if there is an architect on the project, many architects do not issue an ID Set (Interior Design Set). To fill this gap, we have started Varnell Detail Group. Although we are interior designers, we will provide only specification services. By interfacing with the client and contractor, we will provide the client with a schedule and prompt them when it is time to shop. Additionally, we will give them a list of GC preferred vendors for them to shop with. Once selections have been made, specifications will be written, plans will be tagged. This process continues for all the pieces necessary for a home to be built: Plumbing, Appliances, Mouldings, Interior Doors, Cabinets, Hard Surfaces (Including counters, and showers), Flooring, Motorized Window Coverings, Hardware, Room Finish Schedule, Lighting - Recessed, Decorative and Exterior, Electrical Outlets, Exterior Hardscape Materials.

Professional contractors are used to receiving this information. Without the interior designer, the contractor often has to step in to guide the client. This takes him or her away from their actual job of building the house. What this translates to is a project that becomes late and over budget. The cost benefit of the specification process is that the project can be delivered on time, and helps to control the budget. By delivering on time, the homeowner does not incur additional interest charges and other costs involved in construction delays.

I would like a website that is built on a platform that I can edit if I need to do so, without having to call someone else to do it. Perhaps on Wix or Square Space if this is possible. I would like the ability to link social media. Also, if the photos need changing, it should be something simple for me to do. The website should be relatively simple. Show a few photos of the finished product along with the drawings that led up to them. I would also like to show a project spec sheet.

I've uploaded the photos and some of the documentation. The documentation will be a placeholder for the moment. I will change them to reflect the new logo and change the clients name. These will be ready next week, but for now we can use what I'm providing.

I like the "background' squiggle on my logo. Perhaps this can be integrated in some way. The website should tell in a concise manner what we do and who we do it for. It should appeal to the General Contractor, but could also be directed to the homeowner. I have lots of other photos if more are needed, but these are a start. I think too much info on the website won't help.

Target Market(s)

Luxury Home Builders; Professional General Contractors, People building luxury homes or remodeling a luxury property who don't want to use an interior designer.

Industry/Entity Type

Business

Coding

Coded - Design and coding required

Number of Pages Required

4 page

Font styles to use
Other font styles liked:
• Use fonts that work with the logo I sent

Colors
ec1f27
c3c3c3

Requirements
Must have
• Company Name and Logo, About, Contact Us, FAQ, Photos and Specs. Use the files I sent for the Logo, and the colors for the website should be derived from those files. I like clean and simple.
Nice to have
• Builder Testimonials. I am working on getting two.
Should not have
• Not sure until I see it.

```html
<!DOCTYPE html>
<html lang="en">
<head>
<meta charset="utf-8">
<title>Varnell Detail Group – Professional Specifications for Contractors</title>
<link rel="stylesheet" href="https://fonts.googleapis.com/css2?family=Poppins:wght@300;400;500;600&family=Roboto+Condensed:wght@400&display=swap">
<style>
:root{
  --red:#ec1f27;
  --grey:#c3c3c3;
  --ink:#2b2b2b;
  --text:#444;
  --muted:#777;
  --light:#f4f4f4;
  --line:#e3e3e3;
  --footer:#5b5b5b;
  --footer-dark:#3f3f3f;
  --white:#fff;
  --wood-dark:#3b2619;
  --wood:#7a5334;
  --wood-warm:#a87a52;
  --paper:#f7f7f5;
  --paper-edge:#e2e2df;
}
*{box-sizing:border-box;margin:0;padding:0}
html,body{width:1200px;height:3719px;overflow:hidden}
body{font-family:"Poppins",sans-serif;color:var(--text);background:var(--white);position:relative}
.section{position:absolute;left:0;width:1200px}
.center{text-align:center}

/* top bar */
.topbar{top:0;height:45px;background:#f7f7f7;border-bottom:1px solid var(--line);font-size:12px;color:var(--muted)}
.topbar .tagline{position:absolute;left:112px;top:14px}
.topbar .office{position:absolute;left:818px;top:13px;color:var(--ink);font-size:13px}
.topbar .office b{font-weight:500}
.phone-icon{display:inline-block;vertical-align:-2px;margin-right:5px}
.social{position:absolute;display:flex;gap:14px}
.topbar .social{left:1005px;top:16px}
.social span{width:12px;height:12px;border-radius:50%;background:var(--grey);display:block}

/* nav */
.nav{top:45px;height:110px;background:var(--white)}
.brand{position:absolute;display:flex;align-items:center;gap:8px}
.nav .brand{left:112px;top:38px}
.brand-square{width:30px;height:30px;background:#8a3b1f;display:block}
.brand-name{font-size:15px;font-weight:500;color:#5a5a5a;line-height:1.1;letter-spacing:.5px}
.menu{position:absolute;left:645px;top:42px;display:flex;gap:44px;font-size:14px;color:var(--ink)}

/* shared image placeholders */
.frame{box-shadow:inset 0 0 0 14px var(--paper),inset 0 0 0 15px var(--paper-edge)}

/* hero */
.hero{top:155px;height:495px}
.hero-photo{position:absolute;inset:0;background:linear-gradient(100deg,#2e2018 0%,#5a3b26 18%,#9b7048 38%,#c9b49a 55%,#8a5c38 72%,#4a2e1c 100%)}
.hero-shade{position:absolute;inset:0;background:linear-gradient(180deg,rgba(0,0,0,.15),rgba(0,0,0,.35) 50%,rgba(0,0,0,.1))}
.hero h1{position:absolute;top:158px;width:100%;text-align:center;font-family:"Roboto Condensed",sans-serif;font-weight:400;font-size:54px;color:var(--white);text-shadow:0 2px 6px rgba(0,0,0,.5)}
.hero .sub{position:absolute;top:232px;left:190px;width:820px;text-align:center;font-size:21px;line-height:1.45;color:var(--white);text-shadow:0 1px 4px rgba(0,0,0,.5)}
.btn{display:inline-block;font-size:12px;font-weight:500;letter-spacing:.5px;text-transform:uppercase;padding:11px 20px}
.btn-solid{background:var(--red);color:var(--white)}
.btn-outline{border:1px solid var(--red);color:var(--red);background:var(--white)}
.hero .btn{position:absolute;top:320px;left:539px}

/* intro */
.intro{top:650px;height:498px}
.intro h2{position:absolute;top:60px;width:100%;font-weight:300;font-size:33px;color:var(--ink);line-height:1.3}
.intro h2 strong{font-weight:400;display:block}
.intro p{position:absolute;left:128px;width:944px;font-size:12px;line-height:1.9;text-align:center;color:#555}
.intro .p1{top:183px}
.intro .p2{top:315px}
.intro .btn{position:absolute;top:400px;left:539px}

/* concept */
.concept{top:1148px;height:617px;background:var(--light);border-top:1px solid var(--line);border-bottom:1px solid var(--line)}
.concept-photo{position:absolute;left:640px;top:0;width:560px;height:617px;background:linear-gradient(120deg,#4a4038 0%,#7d7670 30%,#a5a09a 48%,#6a5a4c 66%,#3a2a1e 100%)}
.concept h2{position:absolute;left:112px;top:80px;font-size:40px;font-weight:300;color:var(--ink)}
.concept h2 b{font-weight:400}
.step{position:absolute;left:112px;display:flex;gap:18px;align-items:flex-start;width:420px}
.step .thumb{width:86px;flex:none;border:1px solid #cfcfcf}
.step p{font-size:12.5px;line-height:1.65;color:#444;padding-top:6px}
.thumb.plan{background:linear-gradient(135deg,#f1ede4,#d8cfbf)}
.thumb.sheet-thumb{background:linear-gradient(180deg,#fbfbfb,#e8e8e8);box-shadow:inset 0 0 0 6px #fbfbfb,inset 0 0 0 7px #d7d7d7}
.thumb.shower{background:linear-gradient(180deg,#cbbda8,#8e7a63)}
.drawing-card{position:absolute;left:543px;top:156px;width:317px;height:308px;background:var(--white);box-shadow:0 2px 12px rgba(0,0,0,.2)}
.drawing-card .sheet{position:absolute;inset:16px;background:linear-gradient(180deg,#fbfbfb,#ededed);border:1px solid #d9d9d9}

/* projects */
.projects{top:1765px;height:607px}
.section-title{position:absolute;width:100%;text-align:center;font-size:44px;font-weight:300;color:var(--ink)}
.section-title b{font-weight:500}
.section-sub{position:absolute;width:100%;text-align:center;font-size:12.5px;color:#555}
.projects .section-title{top:72px}
.projects .section-sub{top:140px}
.grid{position:absolute;left:112px;top:189px;width:976px;height:360px;display:grid;grid-template-columns:255px 240px 240px 241px;grid-template-rows:180px 180px}
.tile{position:relative}
.tile.photo-a{background:linear-gradient(135deg,#2e1e15 0%,#5b3a28 50%,#8a5a3c 100%)}
.tile.drawing{background:linear-gradient(180deg,#fafafa,#e6e6e6)}
.tile.photo-b{background:linear-gradient(150deg,#3a2418 0%,#7a5234 45%,#b0875e 100%)}
.tile.photo-c{background:linear-gradient(135deg,#2a2522 0%,#5e534b 50%,#8a7e72 100%)}
.tile.photo-d{background:linear-gradient(160deg,#2a1a10 0%,#6b4a2e 50%,#a27c52 100%)}
.caption{position:absolute;background:var(--red);color:var(--white);font-size:11.5px;line-height:1.45;text-align:center;padding:8px 10px;opacity:.94}
.c1{left:91px;top:94px;width:308px}
.c2{left:754px;top:94px;width:204px}
.c3{left:12px;top:278px;width:198px}
.c4{left:508px;top:278px;width:210px}

/* faq */
.faq{top:2372px;height:498px;background:var(--light);border-top:1px solid var(--line)}
.faq .section-title{top:40px}
.faq .section-title .slash{color:#999;font-weight:300}
.faq .section-sub{top:110px}
.faq-list{position:absolute;left:112px;top:151px;width:976px}
.faq-item{background:var(--white);border:1px solid var(--line);margin-bottom:16px;padding:10px 16px;position:relative}
.faq-item h3{font-size:16px;font-weight:400;color:var(--ink);line-height:20px}
.faq-item.open h3{color:var(--red)}
.faq-item p{font-size:12.5px;line-height:1.75;color:#555;margin-top:10px}
.toggle{position:absolute;right:12px;top:12px;width:16px;height:16px;border:1px solid var(--grey);border-radius:50%}
.faq-item.open .toggle{border-color:var(--red)}
.toggle::after{content:"";position:absolute;left:4px;top:7px;width:6px;height:1px;background:var(--grey)}
.faq-item.open .toggle::after{background:var(--red)}

/* testimonials */
.testimonials{top:2870px;height:521px}
.testimonials .section-title{top:52px}
.testimonials .section-sub{top:122px}
.quote{position:absolute;width:471px;top:244px;text-align:center}
.quote .mark{position:absolute;top:-95px;font-size:160px;color:#eeeeee;font-family:Georgia,serif;line-height:1}
.quote .mark.l{left:90px}
.quote .mark.r{right:30px}
.quote p{position:relative;font-size:12.5px;line-height:1.75;color:#444}
.quote .by{margin-top:10px;font-size:12.5px}
.quote .by span{color:var(--red)}
.q1{left:112px}
.q2{left:627px}
.dots{position:absolute;top:430px;left:560px;display:flex;gap:8px}
.dots span{width:12px;height:12px;border-radius:50%;background:var(--grey)}
.dots span:first-child{background:var(--red)}

/* footer */
.footer{top:3391px;height:278px;background:var(--footer);color:#e6e6e6}
.footer .brand{left:112px;top:44px}
.footer .brand-square{background:#8c8c8c}
.footer .brand-name{color:#e6e6e6}
.footer .about{position:absolute;left:112px;top:122px;width:250px;font-size:12.5px;line-height:1.6;color:#d8d8d8}
.footer h4{position:absolute;font-size:17px;font-weight:500;color:var(--white)}
.footer .contact-h{left:466px;top:44px}
.footer .contact{position:absolute;left:466px;top:85px;font-size:12.5px;line-height:1.7;font-weight:500}
.footer .contact .gap{margin-top:12px}
.footer .help{position:absolute;left:466px;top:194px;border:1px solid #cfcfcf;padding:8px 14px;font-size:13px}
.footer .news-h{left:798px;top:44px}
.footer .news-text{position:absolute;left:798px;top:82px;width:270px;font-size:12.5px;line-height:1.6;color:#d8d8d8}
.footer .email{position:absolute;left:798px;top:124px;width:290px;height:43px;background:var(--white);color:#999;font-size:12px;padding:13px 14px}
.footer .subscribe{position:absolute;left:798px;top:179px}
.bottombar{top:3669px;height:50px;background:var(--footer-dark);color:#ddd;font-size:12px}
.bottombar .social{left:112px;top:19px}
.bottombar .social span{background:#aaa}
.bottombar .copy{position:absolute;left:870px;top:17px}
</style>
</head>
<body>

<header class="section topbar">
  <div class="tagline">Providing what contractors need for home builds and remodels</div>
  <div class="office"><svg class="phone-icon" width="12" height="12" viewBox="0 0 24 24"><path fill="#ec1f27" d="M6.6 10.8c1.4 2.8 3.8 5.1 6.6 6.6l2.2-2.2c.3-.3.7-.4 1-.2 1.1.4 2.3.6 3.6.6.6 0 1 .4 1 1V20c0 .6-.4 1-1 1C10.6 21 3 13.4 3 4c0-.6.4-1 1-1h3.5c.6 0 1 .4 1 1 0 1.3.2 2.5.6 3.6.1.3 0 .7-.2 1z"/></svg>Office: <b>760.555.0142</b></div>
  <div class="social"><span></span><span></span><span></span></div>
</header>

<nav class="section nav">
  <div class="brand"><span class="brand-square"></span><span class="brand-name">Varnell Detail Group</span></div>
  <div class="menu"><span>About</span><span>Services</span><span>Testimonials</span><span>FAQ</span><span>Contact us</span></div>
</nav>

<section class="section hero">
  <div class="hero-photo" role="img" aria-label="Photo of a finished luxury kitchen with walnut cabinetry, glass pendant lights, a white island and a mosaic tile wall"></div>
  <div class="hero-shade"></div>
  <h1>Professional Specifications for Contractors</h1>
  <p class="sub">Bridging the Gap Between homeowners and contractors for building or remodeling projects.</p>
  <span class="btn btn-solid">Learn more</span>
</section>

<section class="section intro center">
  <h2>Remodeling or building a home without an interior designer? <strong>We can help!</strong></h2>
  <p class="p1">Homeowners often want to do their own interior design when building or remodeling a home. however, interior designers provide specifications that contractors need when implementing things from structural changes to installing new faucets or tile. without services typically provided by interior designers, individual sub contractors are unable to proceed with their work or to bid the project correctly. We are interior designers that will take client's interior design ideas and plans and turn them into drawings. Schedules and specifications that are required for a successful, on-budget build or remodel, as well as provide them with the resources they'll need to do things themselves.</p>
  <p class="p2">Without the proper drawings and Specifications, it is easy for projects to become late and over budget. let our firm, which has delivered XX projects over XX years, help you keep things on track</p>
  <span class="btn btn-outline">Learn more</span>
</section>

<section class="section concept">
  <div class="concept-photo" role="img" aria-label="Photo of a finished bathroom with a dark wood vanity, crystal chandelier and framed art"></div>
  <h2>From Concept <b>to Reality</b></h2>
  <div class="step" style="top:166px"><span class="thumb plan" style="height:58px" role="img" aria-label="Colored floor plan thumbnail"></span><p>We take the client's ideas and vision and turn them into the tools the contractor and subcontractors need to create their vision.</p></div>
  <div class="step" style="top:270px"><span class="thumb sheet-thumb" style="height:80px" role="img" aria-label="Specification sheet thumbnail"></span><p>Pick from professional interior Designer's sources for foucets, tile cabinets and more</p></div>
  <div class="step" style="top:375px"><span class="thumb shower" style="height:112px" role="img" aria-label="Finished shower photo thumbnail"></span><p>Receive a schedule for what needs to be ordered when, along with prompts and assistance</p></div>
  <div class="drawing-card"><div class="sheet" role="img" aria-label="Technical elevation drawing of bath 2 vanity and shower"></div></div>
</section>

<section class="section projects">
  <h2 class="section-title">Previous <b>Projects</b></h2>
  <p class="section-sub">We have XX years of experience and have completed work on X projects, from totally custom houses to remodels</p>
  <div class="grid">
    <div class="tile photo-a" role="img" aria-label="Photo of a finished dining room with red flowers"></div>
    <div class="tile drawing frame" role="img" aria-label="Floor plan drawing"></div>
    <div class="tile drawing frame" role="img" aria-label="Elevation drawing"></div>
    <div class="tile photo-b" role="img" aria-label="Photo of a finished living room with a wood beam ceiling"></div>
    <div class="tile photo-c" role="img" aria-label="Photo of a finished bathroom"></div>
    <div class="tile drawing frame" role="img" aria-label="Bath 2 and shower plan drawing"></div>
    <div class="tile photo-d" role="img" aria-label="Photo of a finished wall niche with decor"></div>
    <div class="tile drawing frame" role="img" aria-label="Project specification sheet"></div>
    <div class="caption c1">Sorem ipsum dolor sit et, consectetu adipiscing elit, sed diam nonummy nibh euismod tincidunt.</div>
    <div class="caption c2">Dolor sit et, consectetu adipiscing elit, sed diam nonummy nibh euismod tincidunt.</div>
    <div class="caption c3">Dolor sit et, consectetu adipiscing elit, sed diam nonummy nibh euismod tincidunt.</div>
    <div class="caption c4">Dolor sit et, consectetu adipiscing elit, sed diam nonummy nibh euismod tincidunt.</div>
  </div>
</section>

<section class="section faq">
  <h2 class="section-title">Help <span class="slash">/</span> <b>FAQ</b></h2>
  <p class="section-sub">We have XX years of experience and have completed work on X projects, from totally custom houses to remodels</p>
  <div class="faq-list">
    <div class="faq-item"><h3>How do i select lorem ipsum dolar ?</h3><span class="toggle"></span></div>
    <div class="faq-item open"><h3>When building or remodeling a home ?</h3><span class="toggle"></span>
      <p>Homeowners often want to do their own interior design when building or remodeling a home. however, interior designers provide specifications that contractors need when implementing things from structural changes to installing new faucets or tile. without services typically provided by interior designers, individual sub contractors are unable to proceed with their work or to bid the project correctly. We are interior designers that will take client's interior design ideas and plans and turn them into drawings. Schedules and specifications that are required for a successful, on-budget build or remodel, as well as provide them with the resources they'll need to do things themselves.</p></div>
    <div class="faq-item"><h3>How do i select lorem ipsum dolar ?</h3><span class="toggle"></span></div>
  </div>
</section>

<section class="section testimonials">
  <h2 class="section-title">Customer <b>Says</b></h2>
  <p class="section-sub">We have XX years of experience and have completed work on X projects, from totally custom houses to remodels</p>
  <div class="quote q1"><span class="mark l">&ldquo;</span>
    <p>Having a complete set of design drawings and specifications allows us to provide the best possible pricing to our clients while allowing for an efficient construction schedule. Marla Ostrand's design packages provide just that. Her material schedules and drawings provide a concise representation of the home owner's selections and ensure that they get exactly what was specified.</p>
    <p class="by"><span>Glen Harrow</span> - Harrow Crest Luxury Homebuilders</p></div>
  <div class="quote q2"><span class="mark r">&ldquo;</span>
    <p>Having a complete set of design drawings and specifications allows us to provide the best possible pricing to our clients while allowing for an efficient construction schedule. Marla Ostrand's design packages provide just that. Her material schedules and drawings provide a concise representation of the home owner's selections and ensure that they get exactly what was specified.</p>
    <p class="by"><span>Glen Harrow</span> - Harrow Crest Luxury Homebuilders</p></div>
  <div class="dots"><span></span><span></span><span></span><span></span></div>
</section>

<footer class="section footer">
  <div class="brand"><span class="brand-square"></span><span class="brand-name">Varnell Detail Group</span></div>
  <p class="about">Sorem ipsum dolor sitconsectetuer adipiscing elit, sed diam nonu nibh euismod tincidunt magna aliquamerat volutpat. Ut wisi enim ad minim.</p>
  <h4 class="contact-h">Contacts</h4>
  <div class="contact">
    <div>18-240 Mesa Verde Lane Suite B4</div>
    <div>Palm Hollow, CA 92299</div>
    <div class="gap">Cell: &nbsp;760-555-0142</div>
    <div>info@varnelldetail.com</div>
  </div>
  <span class="help">We can help you anywhere!</span>
  <h4 class="news-h">Newsletter</h4>
  <p class="news-text">Sorem ipsum dolor sitconsectetuer adipiscing elit, sed diam.</p>
  <div class="email">Enter your email</div>
  <span class="btn btn-solid subscribe">Subscribe</span>
</footer>

<div class="section bottombar">
  <div class="social"><span></span><span></span><span></span></div>
  <div class="copy">copyrights &copy; All Rights Reserved 2017</div>
</div>

</body>
</html>
```